Studying Effectively To Do List

I am looking to design a new "Study To Do List" for High School students (Ages 15 - 18) . This will be printed as an A4 notepad and so should only be a single A4 page.

The Design will need to be professional and look semi-serious but also be appealing to High school students (Ages 15 - 18) and should NOT be gender specific.

I have attached a word document outlining the structure of the page. The space provided should be large enough that people can write in it comfortably.

The notepad will most likely be printed in black and white but I'm also looking at coloured options - colours should be kept to a minimum.

This will be printed professionally and should also include a 3mm bleed.

The design should also include the business logo (included in the word document)

Target Market(s)

High School students (Ages 15 - 18). Both genders

Industry/Entity Type

Education

Font styles to use
Serif
Sans Serif

Requirements
Must have
• Please see the word document attached.
Should not have
• Too much colour

```html
<!DOCTYPE html>
<html lang="en">
<head>
<meta charset="utf-8">
<title>Study To Do List</title>
<link href="https://fonts.googleapis.com/css2?family=Open+Sans:wght@300;400;600&display=swap" rel="stylesheet">
<style>
  :root {
    --navy: #1f3347;
    --orange: #f47a20;
    --ink: #555555;
    --rule: #5f5f5f;
    --paper: #ffffff;
  }
  html, body { margin: 0; padding: 0; overflow: hidden; }
  body { width: 856px; height: 1200px; background: var(--paper); font-family: "Open Sans", Arial, sans-serif; font-weight: 300; color: var(--ink); }
  .page { position: relative; width: 856px; height: 1200px; overflow: hidden; }
  .side-band { position: absolute; left: 0; top: 0; width: 42px; height: 1200px; background: var(--navy); }
  .brand { position: absolute; left: 358px; top: 74px; width: 180px; display: flex; align-items: center; gap: 8px; }
  .brand-dot { width: 14px; height: 14px; border-radius: 50%; background: var(--orange); }
  .brand-name { font-size: 24px; font-weight: 600; color: var(--navy); letter-spacing: 0.5px; }
  .date { position: absolute; left: 604px; top: 82px; width: 190px; display: flex; align-items: flex-end; font-size: 16px; }
  .date .line { flex: 1; border-bottom: 1px solid var(--rule); margin-left: 4px; height: 17px; }
  .section-head { position: absolute; left: 94px; width: 700px; display: flex; align-items: flex-end; }
  .section-head .tag { background: var(--navy); color: #fff; font-size: 16px; font-weight: 400; line-height: 18px; padding: 0 4px; }
  .section-head .dash { flex: 1; border-bottom: 1px dashed var(--rule); margin-left: 4px; }
  table.grid { position: absolute; left: 94px; width: 700px; border-collapse: collapse; table-layout: fixed; }
  table.grid td, table.grid th { border: 1px solid var(--rule); height: 25px; padding: 0 5px; font-size: 16px; font-weight: 300; text-align: left; color: var(--ink); }
  table.grid th { text-align: center; }
  .lines { position: absolute; left: 94px; width: 700px; }
  .row { display: flex; align-items: flex-end; height: 26px; font-size: 16.5px; }
  .row .fill { flex: 1; border-bottom: 1px solid var(--rule); margin-left: 5px; height: 18px; }
  .row .assess { display: flex; align-items: flex-end; flex: 0 0 364px; }
  .row .due { margin-left: 9px; }
  .row .fill.due-line { margin-left: 1px; }
  .site { position: absolute; left: 0; right: 0; top: 1154px; text-align: center; padding-left: 52px; font-size: 16px; font-weight: 600; letter-spacing: 2.4px; color: #2a2a2a; }
</style>
</head>
<body>
<div class="page">
  <div class="side-band" aria-hidden="true"></div>

  <div class="brand"><span class="brand-dot"></span><span class="brand-name">Northpath</span></div>

  <div class="date">DATE<span class="line"></span></div>

  <div class="section-head" style="top:180px"><span class="tag">REVISION</span><span class="dash"></span></div>
  <table class="grid" style="top:208px">
    <tr><td>1.</td><td>5.</td></tr>
    <tr><td>2.</td><td>6.</td></tr>
    <tr><td>3.</td><td>7.</td></tr>
    <tr><td>4.</td><td>8.</td></tr>
  </table>

  <div class="section-head" style="top:325px"><span class="tag">HOMEWORK</span><span class="dash"></span></div>
  <div class="lines" style="top:344px">
    <div class="row">Subject:<span class="fill"></span></div>
    <div class="row">Task:<span class="fill"></span></div>
    <div class="row">Subject:<span class="fill"></span></div>
    <div class="row">Task:<span class="fill"></span></div>
    <div class="row">Subject:<span class="fill"></span></div>
    <div class="row">Task:<span class="fill"></span></div>
    <div class="row">Subject:<span class="fill"></span></div>
    <div class="row">Task:<span class="fill"></span></div>
    <div class="row">Subject:<span class="fill"></span></div>
    <div class="row">Task:<span class="fill"></span></div>
    <div class="row">Subject:<span class="fill"></span></div>
    <div class="row">Task:<span class="fill"></span></div>
  </div>

  <div class="section-head" style="top:667px"><span class="tag">ASSESSMENTS</span><span class="dash"></span></div>
  <div class="lines" style="top:688px">
    <div class="row"><span class="assess">Assessment:<span class="fill"></span></span><span class="due">Due</span><span class="fill due-line"></span></div>
    <div class="row">Element:<span class="fill"></span></div>
    <div class="row"><span class="assess">Assessment:<span class="fill"></span></span><span class="due">Due</span><span class="fill due-line"></span></div>
    <div class="row">Element:<span class="fill"></span></div>
    <div class="row"><span class="assess">Assessment:<span class="fill"></span></span><span class="due">Due</span><span class="fill due-line"></span></div>
    <div class="row">Element:<span class="fill"></span></div>
    <div class="row"><span class="assess">Assessment:<span class="fill"></span></span><span class="due">Due</span><span class="fill due-line"></span></div>
    <div class="row">Element:<span class="fill"></span></div>
    <div class="row"><span class="assess">Assessment:<span class="fill"></span></span><span class="due">Due</span><span class="fill due-line"></span></div>
    <div class="row">Element:<span class="fill"></span></div>
    <div class="row"><span class="assess">Assessment:<span class="fill"></span></span><span class="due">Due</span><span class="fill due-line"></span></div>
    <div class="row">Element:<span class="fill"></span></div>
  </div>

  <table class="grid" style="top:1011px">
    <colgroup><col style="width:175px"><col style="width:175px"><col style="width:350px"></colgroup>
    <tr><th colspan="2">NOTES</th><th>PRACTICE</th></tr>
    <tr><td>1.</td><td>5.</td><td>1.</td></tr>
    <tr><td>2.</td><td>6.</td><td>2.</td></tr>
    <tr><td>3.</td><td>7.</td><td>3.</td></tr>
    <tr><td>4.</td><td>8.</td><td>4.</td></tr>
  </table>

  <div class="site">northpathstudy.com.au</div>
</div>
</body>
</html>
```